VARNOLA SYSTEMS BUSINESS CARD DESIGN

WE WANT COMPLETE NEW DESIGN OF OUR BUSINESS CARD. WE ARE AN INTEGRATION COMPANY, WHERE WE INTEGRATE IOT/SMART SYSTEMS TO HOMES AND CORPORATE CUSTOMERS. WE SUPPLY AND INSTALL AUTOMATION PRODUCTS. THE FINAL DESIGN SHOULD COMMUNICATE TECHNOLOGY. THE CARD DESIGN SHOULD BE VERY IMPACT FULL. LOGO NEEDS TO BE THERE. IT WOULD NICE IF THE DESIGN WAS CLEAN. COLORS IS UP TO DESIGNER TO PLAY WITH, OR CAN STICK TO CORPORATE COLORS (FOLLOW LOGO). I HAVE ADDED FEW REFERENCE PHOTOS TO DRAW INSPIRATION MAYBE. I HAVE ADDED A HEX DESIGN, ITS NOT NECESSARY TO USE THIS DESIGN, ITS UPTO DESIGNER, JUST ADDED IF NEEDED TO PLAY WITH DESIGN.

Target Market(s)

Private end users and corporate clients

Industry/Entity Type

technology, home automation, home theaters, building management systems, IOT

Contact Information for Business Card

It should include Employee name, personal number, office number, email address, both in English and arabic. DETAILS TO INCLUDE :GERALD MOSSANE, MOBILE 0097150738915,OFFCIE 009714386207, GERALD@VARNOLAHUB.CO

Requirements
Must have
• Should feel like a technology company from design. Details both and in English and arabic (or at least have provision for arabic in design).
Nice to have
• I would like logo on one side, and details on the other side. Logo design side should communicate technology with logo. Other side can be clean just with information or also have some design aspects following from logo side. it would be interesting to see submissions with square design as well (that looks like an app Icon). colors could be of logo, red black grey and white. I have added some designs to draw inspiration from

```html
<!DOCTYPE html>
<html lang="en">
<head>
<meta charset="utf-8">
<title>Varnola Systems Business Card</title>
<link rel="stylesheet" href="https://fonts.googleapis.com/css2?family=Cairo:wght@400;600&family=Michroma&family=Open+Sans:wght@600;700&family=Roboto:wght@400&display=swap">
<style>
  :root {
    --page: #2a2a2a;
    --card-black: #000000;
    --white: #f2f2f2;
    --grey: #b8b8b8;
    --soft-grey: #d8d8d8;
    --accent-red: #e3262f;
    --frame-red: #d9203a;
    --frame-yellow: #e8c317;
    --frame-teal: #1fb59c;
    --frame-blue: #2b5fa8;
    --frame-green: #5fb34a;
    --frame-purple: #6b2c7a;
  }
  html, body {
    margin: 0;
    padding: 0;
    width: 1200px;
    height: 1138px;
    overflow: hidden;
    background: var(--page);
  }
  .canvas {
    position: relative;
    width: 1200px;
    height: 1138px;
  }
  .card {
    position: absolute;
    width: 622px;
    height: 374px;
  }
  .card--front { left: 272px; top: 184px; }
  .card--back  { left: 274px; top: 606px; width: 620px; height: 376px; }

  .card__frame {
    position: absolute;
    inset: 0;
    background: linear-gradient(135deg, var(--frame-yellow) 0%, var(--frame-teal) 18%, var(--frame-purple) 32%, var(--frame-red) 46%, var(--frame-green) 60%, var(--frame-blue) 74%, var(--frame-yellow) 88%, var(--frame-red) 100%);
  }
  .card__face {
    position: absolute;
    left: 13px; top: 10px; right: 13px; bottom: 11px;
    background: var(--card-black);
  }

  /* Logo side */
  .brand-mark {
    position: absolute;
    inset: 0;
    display: flex;
    align-items: center;
    justify-content: center;
    gap: 16px;
  }
  .brand-mark__dot {
    width: 46px; height: 46px;
    border-radius: 50%;
    background: var(--accent-red);
  }
  .brand-mark__name {
    font-family: "Michroma", sans-serif;
    font-size: 26px;
    color: var(--white);
    letter-spacing: 2px;
  }

  /* Details side */
  .company {
    position: absolute;
    left: 36px; top: 40px;
    display: flex;
    align-items: center;
    gap: 16px;
  }
  .company__dot {
    width: 44px; height: 44px;
    border-radius: 50%;
    background: var(--accent-red);
    flex: none;
  }
  .company__text { display: flex; flex-direction: column; }
  .company__name {
    font-family: "Open Sans", sans-serif;
    font-weight: 700;
    font-size: 42px;
    line-height: 46px;
    letter-spacing: 4px;
    color: var(--white);
  }
  .company__sub {
    font-family: "Open Sans", sans-serif;
    font-weight: 700;
    font-size: 20px;
    line-height: 24px;
    letter-spacing: 1px;
    color: var(--grey);
    margin-left: 12px;
  }
  .tagline {
    position: absolute;
    left: 30px; top: 136px;
    margin: 0;
    font-family: "Michroma", sans-serif;
    font-size: 14px;
    letter-spacing: 3px;
    color: var(--white);
  }

  .arabic {
    position: absolute;
    right: 24px; top: 30px;
    width: 180px;
    margin: 0;
    font-family: "Cairo", sans-serif;
    text-align: right;
    color: var(--soft-grey);
  }
  .arabic__name {
    display: block;
    font-weight: 600;
    font-size: 19px;
    line-height: 28px;
    color: var(--grey);
  }
  .arabic__line {
    display: block;
    font-weight: 400;
    font-size: 14px;
    line-height: 24px;
  }
  .arabic__num { unicode-bidi: isolate; direction: ltr; }

  .person {
    position: absolute;
    left: 25px; top: 248px;
    margin: 0;
    font-family: "Open Sans", sans-serif;
    font-weight: 600;
    font-size: 23px;
    color: var(--grey);
  }
  .contact {
    position: absolute;
    display: flex;
    align-items: center;
    gap: 9px;
    font-family: "Roboto", sans-serif;
    font-size: 16px;
    line-height: 19px;
    letter-spacing: 0.6px;
    color: var(--soft-grey);
  }
  .contact svg { width: 14px; height: 14px; flex: none; }
  .contact--mobile { left: 32px; top: 289px; }
  .contact--office { left: 32px; top: 313px; }
  .contact--email  { left: 203px; top: 289px; }
  .contact--web    { left: 203px; top: 313px; }

  .corner-name {
    position: absolute;
    right: 24px; top: 300px;
    font-family: "Open Sans", sans-serif;
    font-weight: 700;
    font-size: 22px;
    letter-spacing: 3px;
    color: var(--white);
  }
</style>
</head>
<body>
<main class="canvas">

  <section class="card card--front" aria-label="Business card, logo side">
    <div class="card__frame" role="img" aria-label="Multicoloured low-poly geometric border pattern"></div>
    <div class="card__face">
      <div class="brand-mark">
        <span class="brand-mark__dot"></span>
        <span class="brand-mark__name">VARNOLA SYSTEMS</span>
      </div>
    </div>
  </section>

  <section class="card card--back" aria-label="Business card, details side">
    <div class="card__frame" role="img" aria-label="Multicoloured low-poly geometric border pattern"></div>
    <div class="card__face">
      <div class="company">
        <span class="company__dot"></span>
        <span class="company__text">
          <span class="company__name">VARNOLA</span>
          <span class="company__sub">SYSTEMS</span>
        </span>
      </div>
      <p class="tagline">A VARNOLA GROUP DIVISION.</p>

      <p class="arabic" lang="ar" dir="rtl">
        <span class="arabic__name">جيرالد موسان</span>
        <span class="arabic__line">جوال: <span class="arabic__num">0097150738915</span></span>
        <span class="arabic__line">مكتب: <span class="arabic__num">009714386207</span></span>
        <span class="arabic__line">فارنولا سيستمز</span>
      </p>

      <p class="person">Gerald Mossane</p>

      <div class="contact contact--mobile">
        <svg viewBox="0 0 14 14" aria-hidden="true"><rect x="3.5" y="1" width="7" height="12" rx="1.2" fill="none" stroke="#e3262f" stroke-width="1.4"/><circle cx="7" cy="10.8" r="0.8" fill="#e3262f"/></svg>
        <span>0097150738915</span>
      </div>
      <div class="contact contact--office">
        <svg viewBox="0 0 14 14" aria-hidden="true"><circle cx="7" cy="7" r="6" fill="none" stroke="#e3262f" stroke-width="1.2"/><path d="M4.6 4.2l1.2-.4.9 1.7-.7.7c.4.9 1 1.5 1.9 1.9l.7-.7 1.7.9-.4 1.2c-2.9.1-5.4-2.4-5.3-5.3z" fill="#e3262f"/></svg>
        <span>009714386207</span>
      </div>
      <div class="contact contact--email">
        <svg viewBox="0 0 14 14" aria-hidden="true"><rect x="1" y="3" width="12" height="8.5" fill="none" stroke="#e3262f" stroke-width="1.3"/><path d="M1 3.2l6 4.6 6-4.6" fill="none" stroke="#e3262f" stroke-width="1.3"/></svg>
        <span>gerald@varnolahub.co</span>
      </div>
      <div class="contact contact--web">
        <svg viewBox="0 0 14 14" aria-hidden="true"><g fill="none" stroke="#e3262f" stroke-width="1.1"><circle cx="7" cy="7" r="5.8"/><ellipse cx="7" cy="7" rx="2.6" ry="5.8"/><path d="M1.2 7h11.6M2 4h10M2 10h10"/></g></svg>
        <span>www.varnolahub.co</span>
      </div>

      <span class="corner-name">VARNOLA</span>
    </div>
  </section>

</main>
</body>
</html>
```